Logo and business card

RVK Financial Solutions - Branding & Image Project

There will be 3 companies in our group. We want a similar Branding look & feel for all 3. The first company is DLW Financial which is already established, and I have included samples of the branding.

The goal for this design project is to create the corporate branding for RVK Financial Solutions which is the second company in the group.

Please use the same colours and fonts that we use at DLW Financial but the logo must be different. The final design should communicate financial safety and growth. Our typical clients are 40+ years and financially conservative.

Can you create a sample version using the dark green in the attached image.

We will need print resolution files and low res file for email, web etc.

The main printed outputs we need are – see separate attachment for examples;
Business Card 2 sided
Web logo

We’ll then need the following
Letterhead & follow on sheets
Envelopes C5 2 sided & C4 2 sided
Compliment Slips

```html
<!DOCTYPE html>
<html lang="en">
<head>
<meta charset="utf-8">
<title>RVK Financial Solutions – Business Card</title>
<link rel="stylesheet" href="https://fonts.googleapis.com/css2?family=Open+Sans:wght@300;400;600;700&family=Arimo:wght@400&display=swap">
<style>
  :root {
    --gold: #be8a3e;
    --paper: #f7f7f6;
    --ink: #1e1e1e;
    --rule: #dcdcdc;
    --backdrop: #e2e2e2;
    --white: #ffffff;
  }
  * { box-sizing: border-box; margin: 0; padding: 0; }
  html, body { width: 1200px; height: 930px; overflow: hidden; }
  body {
    background: var(--backdrop);
    font-family: "Open Sans", sans-serif;
    display: flex;
    align-items: center;
    justify-content: center;
    gap: 50px;
  }
  .card {
    position: relative;
    width: 540px;
    height: 340px;
    box-shadow: 0 6px 18px rgba(0,0,0,0.12);
  }
  .card--front { background: var(--paper); color: var(--ink); }
  .card--back { background: var(--gold); color: var(--white); }

  /* Wordmark */
  .wordmark { position: absolute; display: flex; align-items: center; gap: 12px; }
  .wordmark__dot { width: 34px; height: 34px; border-radius: 50%; flex: none; }
  .wordmark__name { font-weight: 300; font-size: 25px; letter-spacing: 0.2px; white-space: nowrap; }
  .card--front .wordmark { right: 30px; top: 62px; }
  .card--front .wordmark__dot { background: var(--gold); }
  .card--front .wordmark__name { color: var(--ink); }
  .card--back .wordmark { left: 100px; top: 118px; }
  .card--back .wordmark__dot { background: var(--white); }
  .card--back .wordmark__name { color: var(--white); }

  /* Contact block */
  .contact { position: absolute; left: 30px; top: 30px; }
  .contact__name { color: var(--gold); font-weight: 600; font-size: 22px; line-height: 1.1; }
  .contact__role { font-size: 13px; margin-top: 3px; margin-bottom: 12px; }
  .contact__list { list-style: none; }
  .contact__item { display: flex; align-items: center; gap: 8px; font-size: 13.5px; line-height: 20px; }
  .contact__icon { width: 14px; height: 14px; flex: none; }
  .accent { color: var(--gold); }

  .divider { position: absolute; left: 30px; right: 30px; top: 208px; height: 1px; background: var(--rule); }

  .address {
    position: absolute; right: 30px; bottom: 26px;
    text-align: right; font-size: 14px; line-height: 19px;
  }

  .legal {
    position: absolute; left: 100px; top: 190px;
    font-family: "Arimo", sans-serif; font-size: 10px; line-height: 13px;
    text-align: center; width: 300px;
  }
</style>
</head>
<body>

  <section class="card card--front" aria-label="Business card front">
    <div class="contact">
      <h1 class="contact__name">Morgan Ellery</h1>
      <p class="contact__role">Senior Wealth Adviser</p>
      <ul class="contact__list">
        <li class="contact__item">
          <svg class="contact__icon" viewBox="0 0 14 14" aria-hidden="true"><rect width="14" height="14" rx="2" fill="#be8a3e"/><path d="M4 3.5c-.6.6-.6 1.8.6 3.4 1.2 1.6 2.6 2.8 3.9 3.4.8.3 1.4 0 1.8-.6l-1.4-1.4-.9.6c-.7-.4-1.4-1.1-1.9-1.9l.6-.9L5.3 3z" fill="#fff"/></svg>
          01632 960418
        </li>
        <li class="contact__item">
          <svg class="contact__icon" viewBox="0 0 14 14" aria-hidden="true"><rect width="14" height="14" rx="2" fill="#be8a3e"/><rect x="4.5" y="2.5" width="5" height="9" rx="1" fill="#fff"/><rect x="5.4" y="3.6" width="3.2" height="5.6" fill="#be8a3e"/></svg>
          07700 900315
        </li>
        <li class="contact__item">
          <svg class="contact__icon" viewBox="0 0 14 14" aria-hidden="true"><rect width="14" height="14" rx="2" fill="#be8a3e"/><rect x="2.5" y="4" width="9" height="6" fill="#fff"/><path d="M2.5 4l4.5 3.5L11.5 4" stroke="#be8a3e" stroke-width="0.9" fill="none"/></svg>
          morgan.ellery@rvkfs.co.uk
        </li>
        <li class="contact__item">
          <svg class="contact__icon" viewBox="0 0 14 14" aria-hidden="true"><rect width="14" height="14" rx="2" fill="#be8a3e"/><circle cx="7" cy="7" r="4" fill="none" stroke="#fff" stroke-width="1"/><path d="M3 7h8M7 3c-1.6 2.4-1.6 5.6 0 8M7 3c1.6 2.4 1.6 5.6 0 8" stroke="#fff" stroke-width="0.8" fill="none"/></svg>
          <span>www.<span class="accent">rvkfs</span>.co.uk</span>
        </li>
      </ul>
    </div>

    <div class="wordmark">
      <span class="wordmark__dot"></span>
      <span class="wordmark__name">rvk financial solutions</span>
    </div>

    <div class="divider"></div>

    <address class="address" style="font-style: normal;">
      The Mill House, Unit 4<br>
      Ashford Lane Business Park<br>
      Brookfield Road, Calderton<br>
      Northwick, Herts, NW4 7QX
    </address>
  </section>

  <section class="card card--back" aria-label="Business card back">
    <div class="wordmark">
      <span class="wordmark__dot"></span>
      <span class="wordmark__name">rvk financial solutions</span>
    </div>
    <p class="legal">
      RVK Financial Solutions Limited is authorised and regulated<br>
      by the Financial Conduct Authority reference 612048.<br>
      Registered in England and Wales No. 583917
    </p>
  </section>

</body>
</html>
```